Redesign of Plastic Surgeon Website to fully responsive / modern feel

Hi

Our current website is out of date www.harbourlinecosmetic.org

We want a fresh / modern looking design
Needs to be fully responsive design that works extremely well on ipad and mobile device

Would like design for both full screen website and mobile

Have listed a few websites of other plastic surgeons we like
http://www.reformclinicdaily.com/
http://www.peterholtbymd.com/
http://www.corvanbeauty.com/
http://www.tidewellcontouring.com/

Menu needs to include
1. About Us
2. Procedures (see current website for example)
3. News
4. Patient Resources
5. Contact Us

We are flexible with colours / images / layout

I have uploaded a document that has some content - the face pages content is completed only

some of the procedures can have content upwards of 4000 words - total website can be large with over 40,000 words
Updates

Target Market(s)

Mainly women 20-60 85% of practice
Some men 15%

Industry/Entity Type

Plastic Surgery

Number of Pages Required

5+ page

Requirements
Must have
• We need designs for
• Homepage
• Internal pages
• 1. Landing pages for breast / body / face / non surgical main pages
• 2. Procedure pages for individual pages under each section - eg breast augmentation
• 3. About us pages - like meet the doctor, our staff, clinics
• 4. Contact page
• 5. Blog / News page
Nice to have
• See our list of websites for examples of designs we like
• Like full screen design with nice hero image
• Needs to have good to call to action messages on home page like
• Specials, procedure of the month, etc

```html
<!DOCTYPE html>
<html lang="en">
<head>
<meta charset="utf-8">
<title>Facelift | Harbourline Institute of Cosmetic Surgery</title>
<link rel="stylesheet" href="https://fonts.googleapis.com/css2?family=Raleway:wght@400;500;600;700&family=Open+Sans:wght@400;600;700&display=swap">
<style>
:root{
  --orange:#d4612a;
  --tan:#c9a784;
  --teal:#9dd9d0;
  --brown:#5a4b3f;
  --ink:#3d3d3d;
  --muted:#8a8a8a;
  --line:#e4e4e4;
  --band:#f1f1f1;
  --acc:#ececec;
  --side:#a9a9a9;
  --dark:#2b2623;
}
*{box-sizing:border-box;margin:0;padding:0}
html,body{width:1200px;height:3333px;overflow:hidden}
body{font-family:"Open Sans",Arial,sans-serif;color:var(--ink);background:#fff;position:relative}
h1,h2,h3,h4{font-family:"Raleway",Arial,sans-serif;font-weight:500}

/* header */
.site-header{position:absolute;top:0;left:0;width:1200px;height:127px;background:#fff}
.brand{position:absolute;left:134px;top:0;width:332px;height:127px;background:#fff;box-shadow:0 2px 6px rgba(0,0,0,.15);display:flex;align-items:center;gap:12px;padding-left:34px}
.brand-dot{width:22px;height:22px;border-radius:50%;background:var(--orange);flex:none}
.brand-name{font-family:"Raleway",sans-serif;font-size:21px;font-weight:500;color:var(--brown);line-height:1.15}
.call-bar{position:absolute;left:744px;top:0;width:367px;height:44px;background:#d9d9d9;display:flex;align-items:center;justify-content:center;gap:12px;color:#fff;font-size:15px;font-weight:600;letter-spacing:.5px}
.call-bar strong{color:var(--orange);font-size:19px;margin-left:4px}
.main-nav{position:absolute;top:86px;left:520px;display:flex;gap:28px;font-family:"Raleway",sans-serif;font-size:12.5px;font-weight:600;color:#555}
.main-nav .active{color:var(--orange)}
.main-nav span small{font-size:9px}

/* title band */
.page-title{position:absolute;top:127px;left:0;width:1200px;height:95px;background:var(--band)}
.page-title h1{position:absolute;left:82px;top:20px;font-size:33px;color:var(--brown)}
.crumbs{position:absolute;left:84px;top:69px;font-size:11px;color:#aaa}
.colour-strip{position:absolute;top:222px;left:0;width:1200px;height:8px;display:flex}
.colour-strip i{flex:1}

/* sidebar */
.side-nav{position:absolute;top:267px;left:84px;width:238px}
.side-nav a{display:block;height:38px;margin-bottom:2px;background:var(--side);color:#fff;font-family:"Raleway",sans-serif;font-size:11.5px;font-weight:700;padding:12px 10px;text-decoration:none;letter-spacing:.3px}
.side-nav a.current{background:var(--orange)}

/* main */
.content{position:absolute;top:262px;left:349px;width:762px}
.content h2{font-size:27px;color:#333}
.intro{font-size:11.5px;line-height:1.62;color:var(--muted);margin-top:4px}
.content h3{font-size:22px;color:#444;margin-top:22px}
.facts{list-style:none;margin-top:8px}
.facts li{font-size:11.5px;line-height:1.6;color:var(--muted);padding-left:22px;position:relative;margin-bottom:3px}
.facts li::before{content:"";position:absolute;left:2px;top:5px;width:9px;height:9px;border-radius:50%;background:#222}
.facts b{color:#333}
.treatment{font-size:22px;margin-top:26px!important}

.accordion{margin-top:12px}
.acc-row{height:26px;margin-bottom:2px;background:var(--acc);display:flex;align-items:center;justify-content:space-between;padding:0 14px;font-size:11.5px;color:#555}
.acc-row svg{width:12px;height:12px}
.acc-row.open{background:var(--orange);color:#fff}
.acc-panel{height:1360px;overflow:hidden;background:#f7f7f7;padding:16px 18px 0 18px;margin-bottom:4px}
.acc-panel h4{font-size:18px;color:#333;margin:4px 0 10px}
.acc-panel ul{list-style:none}
.acc-panel li{position:relative;padding-left:24px;font-size:10.6px;line-height:1.72;color:#888;margin-bottom:20px}
.acc-panel li::before{content:"";position:absolute;left:6px;top:7px;width:6px;height:6px;border-radius:50%;background:#999}
.costs{font-size:22px;margin-top:28px!important}
.costs-text{font-size:11.5px;color:var(--muted);margin-top:6px}
.costs-text a{color:#333;text-decoration:none}

/* partners */
.partners{position:absolute;top:2578px;left:0;width:1200px;height:189px;background:#f6f6f6;display:flex;align-items:center;justify-content:center;gap:58px}
.badge{width:96px;height:70px;background:#cfd4dc;border-radius:6px}
.badge.round{border-radius:50%;width:76px;height:76px;background:#c2cde0}
.badge.red{background:#e3c3c5}
.badge.crest{width:52px;height:82px;background:#d9c9b2;border-radius:8px 8px 26px 26px}

/* categories */
.categories{position:absolute;top:2767px;left:0;width:1200px;height:244px;display:flex}
.cat{flex:1;display:flex;align-items:center;justify-content:center;color:#fff;font-family:"Raleway",sans-serif;font-size:21px;font-weight:700;text-shadow:0 1px 3px rgba(0,0,0,.3)}
.cat.face{background:linear-gradient(135deg,#7b6a60,#d9b8a3)}
.cat.breast{background:linear-gradient(135deg,#c9a497,#8e6f68)}
.cat.body{background:linear-gradient(135deg,#b5a7a1,#dccfc6)}
.cat.nonsurg{background:linear-gradient(135deg,#b58a72,#e3c8b6)}

/* footer */
.site-footer{position:absolute;top:3011px;left:0;width:1200px;height:278px;background:var(--dark);color:#ddd}
.site-footer h4{font-size:22px;color:#fff}
.sitemap{position:absolute;left:84px;top:50px}
.sitemap ul{list-style:none;margin-top:12px}
.sitemap li{font-size:12.5px;line-height:1.5}
.news{position:absolute;left:262px;top:50px;width:360px}
.news-item{display:flex;gap:14px;margin-top:12px}
.thumb{width:104px;height:62px;flex:none;background:linear-gradient(135deg,#e8c9b0,#f6e6d8)}
.news-item h5{font-family:"Raleway",sans-serif;font-size:13px;color:var(--orange);font-weight:600}
.news-item p{font-size:11.5px;line-height:1.4;color:#ccc;margin-top:4px}
.view-all{position:absolute;left:245px;top:146px;width:104px;height:28px;background:var(--orange);color:#fff;font-size:11px;font-weight:600;display:flex;align-items:center;justify-content:center}
.clinic{position:absolute;left:667px;top:50px;width:460px}
.clinic-cols{display:flex;gap:34px;margin-top:10px}
.clinic-cols div{font-size:11px;line-height:1.45;width:118px}
.clinic-cols b{display:block;color:var(--orange);font-size:14px;font-weight:600}
.legal{position:absolute;top:3289px;left:0;width:1200px;height:44px;background:var(--orange);color:#fff;font-size:10px;display:flex;align-items:center;justify-content:center}
</style>
</head>
<body>

<header class="site-header">
  <div class="brand"><span class="brand-dot"></span><span class="brand-name">Harbourline Institute<br>of Cosmetic Surgery</span></div>
  <div class="call-bar">
    <svg width="18" height="18" viewBox="0 0 24 24"><path fill="#fff" d="M6.6 10.8a15 15 0 006.6 6.6l2.2-2.2c.3-.3.7-.4 1-.2 1.1.4 2.3.6 3.6.6.6 0 1 .4 1 1V20c0 .6-.4 1-1 1A17 17 0 013 4c0-.6.4-1 1-1h3.5c.6 0 1 .4 1 1 0 1.3.2 2.5.6 3.6.1.3 0 .7-.2 1z"/></svg>
    CALL FOR APPOINTMENTS: <strong>02 9000 4417</strong>
  </div>
  <nav class="main-nav">
    <span>ABOUT US <small>▾</small></span>
    <span class="active">PROCEDURES <small>▾</small></span>
    <span>PATIENT RESOURCES <small>▾</small></span>
    <span>NEWS / BLOGS</span>
    <span>CONTACT US</span>
  </nav>
</header>

<section class="page-title">
  <h1>Procedures</h1>
  <p class="crumbs">Procedures » Face » Facelift</p>
</section>
<div class="colour-strip"><i style="background:var(--tan)"></i><i style="background:var(--teal)"></i><i style="background:var(--orange)"></i><i style="background:var(--brown)"></i></div>

<nav class="side-nav">
  <a class="current">FACELIFT</a>
  <a>MEET DR CALLOWAY</a>
  <a>OUR PHILOSOPHY AND VALUES</a>
  <a>OUR STAFF</a>
  <a>LOCATIONS</a>
</nav>

<main class="content">
  <h2>Facelift</h2>
  <p class="intro">Over the last few decades there has been an abundance of new techniques, technologies, and treatments introduced for face and neck enhancement, making the path to rejuvenation even more confusing. To bring clarity to this process, I create a comprehensive treatment plan for every patient that includes the newest technologies and treatment options. This takes into account the different aspects of your lifestyle, anatomy, and expectations, while ensuring to maintain your natural beauty. Overall, it is a fully-integrated program that provides the most desirable outcome with the least amount of surgical intervention and downtime.</p>

  <h3>Quick Facts</h3>
  <ul class="facts">
    <li><b>Anesthesia:</b> General Anaesthesia</li>
    <li><b>In/Outpatient:</b> Inpatient</li>
    <li><b>Length of surgery:</b> 3-5 hours</li>
    <li><b>Recovery:</b> – Most patients are back to work in approximately 10 - 14 days when swelling and bruising resolves. We advise our patients to avoid strenuous activity for 1 month.</li>
    <li><b>Results:</b> – Final results are seen within 6 months, and the duration of those results vary from one person to another due to the quality of their skin, ageing and weight changes.</li>
  </ul>

  <h3 class="treatment">Your Treatment at Harbourline Cosmetic Institute</h3>
  <div class="accordion">
    <div class="acc-row">Facelift Surgery<svg viewBox="0 0 12 12"><path d="M2 8l4-4 4 4" fill="none" stroke="#444" stroke-width="2"/></svg></div>
    <div class="acc-row">Early Facelifts<svg viewBox="0 0 12 12"><path d="M2 8l4-4 4 4" fill="none" stroke="#444" stroke-width="2"/></svg></div>
    <div class="acc-row">Modern Facelifts<svg viewBox="0 0 12 12"><path d="M2 8l4-4 4 4" fill="none" stroke="#444" stroke-width="2"/></svg></div>
    <div class="acc-row">SMAS procedure<svg viewBox="0 0 12 12"><path d="M2 8l4-4 4 4" fill="none" stroke="#444" stroke-width="2"/></svg></div>
    <div class="acc-row">How can I expect to look?<svg viewBox="0 0 12 12"><path d="M2 8l4-4 4 4" fill="none" stroke="#444" stroke-width="2"/></svg></div>
    <div class="acc-row">When can I resume social activities?<svg viewBox="0 0 12 12"><path d="M2 8l4-4 4 4" fill="none" stroke="#444" stroke-width="2"/></svg></div>
    <div class="acc-row">Healing<svg viewBox="0 0 12 12"><path d="M2 8l4-4 4 4" fill="none" stroke="#444" stroke-width="2"/></svg></div>
    <div class="acc-row">Will everyone know I've had a Facelift?<svg viewBox="0 0 12 12"><path d="M2 8l4-4 4 4" fill="none" stroke="#444" stroke-width="2"/></svg></div>
    <div class="acc-row">When should I have a Facelift?<svg viewBox="0 0 12 12"><path d="M2 8l4-4 4 4" fill="none" stroke="#444" stroke-width="2"/></svg></div>
    <div class="acc-row">How long will it last?<svg viewBox="0 0 12 12"><path d="M2 8l4-4 4 4" fill="none" stroke="#444" stroke-width="2"/></svg></div>
    <div class="acc-row">Is it painful?<svg viewBox="0 0 12 12"><path d="M2 8l4-4 4 4" fill="none" stroke="#444" stroke-width="2"/></svg></div>
    <div class="acc-row">How will I feel afterwards?<svg viewBox="0 0 12 12"><path d="M2 8l4-4 4 4" fill="none" stroke="#444" stroke-width="2"/></svg></div>
    <div class="acc-row open">Understanding the risks and complications<svg viewBox="0 0 12 12"><path d="M2 4l4 4 4-4" fill="none" stroke="#fff" stroke-width="2"/></svg></div>

    <div class="acc-panel">
      <h4>Possible side effects</h4>
      <ul>
        <li>Swelling – this is normal following facelift surgery, reaches a maximum at about three days and usually lasts up to three weeks and very occasionally six to eight weeks.</li>
        <li>Pigmentation (discolouration and bruising) – bruising usually comes to the surface within a few days and then gradually resolves over two to three weeks. Occasionally extensive bruising can require many weeks or months to totally resolve. These problems can be common in patients with thin, hypo-pigmented, transparent skin. Patients with darker complexions should be aware of the possibility of residual brown pigmentation. Should this occur, there are treatments which will accelerate its resolution, but they take some time to have an effect.</li>
        <li>Loss of or abnormal sensation – it is usual to have a reduction in skin sensation after a facelift procedure. This can include the skin around the cheeks, chin and neck and it is also possible to have numbness of the lower portion of the ear and the hairline, both above and below the ears. Feeling will usually return over a period of 8 – 12 weeks, but in some patients this does take a little longer. A feeling of "insects crawling under the skin" can be experienced while the sensations are returning and this should be considered normal. On rare occasions, sensation can be increased and this will slowly return to normal over a period of weeks to months.</li>
        <li>Tightness, vice-like feelings, headaches – when the superficial muscle layer of the neck is tightened, occasionally a feeling of tightness or choking can be experienced. This is not usually a permanent problem as the muscle layer and sutures do tend to loosen slightly and the feeling of tightness around the neck reduces. However, during the week or weeks that this is present it can be a disconcerting feeling. The same applies to the area around the upper cheeks and temple and occasionally behind the ear. A vice-like feeling in this area and headaches can be experienced. Again, these settle as the swelling reduces and the tissues soften and relax. Significant pain is not common after facelift surgery and if it is experienced, it is mostly temporary.</li>
        <li>Alteration of the hairline – may occur especially in the side-burn areas. Dr Calloway will discuss with you his technique to minimise this often troublesome problem. Male patients should be aware that the hairless area in the front of the ear may be narrowed and that the beard pattern will possibly change, necessitating shaving closer to the ear at the front and maybe behind the ear. Dr Calloway modifies his incisions to prevent as far as possible any alteration to the normal "geography" of the hair line.</li>
        <li>Hair loss – as a result of anaesthesia or the facelift surgery may occur in the temple area or behind the ear. This is usually temporary with normal regrowth noted within several months.</li>
        <li>Scarring – will occur whenever skin is incised and of course all effort is made to place scar lines where they will not be detected by the unknowing observer. Scar maturation varies from person to person and occurs over 3-12 months. Scars normally progress through red, itchy, lumpy, white and leathery stages before settling to their final state. Visible incision lines may tend to thicken; require steroid injections or pressure therapy and possibly additional revision surgery will be indicated to improve the result.</li>
        <li>Broken capillaries – with any skin lifting surgery, it is possible to cause some broken capillaries in the skin. This is more so if this condition already exists and can be noticeable on the lower cheeks and neck area. Fortunately laser treatment is available for improving the appearance of broken capillaries and this would require referral to a specialist who deals with this problem.</li>
      </ul>
      <h4>Possible complications</h4>
      <ul>
        <li>Infection – this is extremely rare despite the proximity of hair around the wound, as the face has an excellent blood supply. Antibiotics may be administered to further minimise this possibility where indicated.</li>
        <li>Blood clots or haematoma – although all care is taken to minimise bleeding, occasionally a blood vessel will continue to bleed after surgery producing a swelling or mass of blood (usually clotted). This clot or haematoma is usually noted within the first 24 to 48 hours after facelift surgery and may require further surgical exploration to drain the collection and stop the bleeding if it is sufficiently large. Small amounts of bleeding may leave an indurated or thickened area for a few months. This may respond to ultrasound treatment, but should settle without affecting the long term result.</li>
        <li>Skin death (necrosis) – fortunately skin death (or necrosis) is a very rare complication of facelift surgery. However, even with the best operating skill it can occur. The area most frequently involved is the non hair-bearing skin behind the ear. If this was to occur, the area would be allowed to heal. Occasionally small skin grafts are necessary to speed up the healing process. If skin death does occur, additional scarring would result and would appear as white scar after maturation has occurred. Usually as the skin becomes looser the scar can be reduced in size and the effects of this complication can often be minimised. This complication is much more common in smokers and has been estimated to be 12 times more likely than in non-smokers. You should therefore inform Dr Calloway if you are a smoker.</li>
        <li>Nerve damage – possible nerve damage involving the sensory nerves to the cheek, neck and ear area has been covered earlier. However, damage to the nerves which innervate the muscles of the face can infrequently occur and it has been estimated to occur in approximately 0.7% of all facelifts. This will cause facial distortion or weakness around the eyebrows or mouth. This is transient in most cases and usually returns to normal over the first 6 weeks to 6 months. Occasionally this can persist as a permanent complication which will compromise the beneficial goals of the procedure. Damage to these motor nerves is slightly more common when the SMAS procedure is used. This is why the operation takes longer and requires a greater degree of skill.</li>
      </ul>
    </div>

    <div class="acc-row">Prior to Facelift surgery<svg viewBox="0 0 12 12"><path d="M2 8l4-4 4 4" fill="none" stroke="#444" stroke-width="2"/></svg></div>
    <div class="acc-row">After Facelift surgery<svg viewBox="0 0 12 12"><path d="M2 8l4-4 4 4" fill="none" stroke="#444" stroke-width="2"/></svg></div>
  </div>

  <h3 class="costs">Facelift Treatment Costs</h3>
  <p class="costs-text">For facelift treatment fees, call Harbourline Cosmetic Institute at 02 xxxx or email us at <a>info@harbourlinecosmetic.org</a>.</p>
</main>

<section class="partners" aria-label="Professional memberships">
  <div class="badge"></div>
  <div class="badge round"></div>
  <div class="badge red"></div>
  <div class="badge crest"></div>
  <div class="badge"></div>
  <div class="badge round"></div>
  <div class="badge round"></div>
</section>

<section class="categories">
  <div class="cat face" role="img" aria-label="Photo of a woman's face, procedure category Face">Face</div>
  <div class="cat breast" role="img" aria-label="Photo of a woman's shoulder and chest, procedure category Breast">Breast</div>
  <div class="cat body" role="img" aria-label="Photo of a woman's back, procedure category Body">Body</div>
  <div class="cat nonsurg" role="img" aria-label="Photo of a woman's skin close-up, procedure category Non-Surgical">Non-Surgical</div>
</section>

<footer class="site-footer">
  <div class="sitemap">
    <h4>Sitemap</h4>
    <ul><li>Home</li><li>About Us</li><li>Procedures</li><li>Patient Resources</li><li>News / Blog</li><li>Contact Us</li></ul>
  </div>
  <div class="news">
    <h4>Latest News / Blogs</h4>
    <div class="news-item">
      <div class="thumb" role="img" aria-label="Photo of a woman's abdomen"></div>
      <div>
        <h5>Who should have a tummy tuck?</h5>
        <p>After giving birth or losing heaps of weight, many women find the shape of their tummy has dramatically changed and, no matter how much cardio ..</p>
      </div>
    </div>
    <div class="view-all">VIEW ALL</div>
  </div>
  <div class="clinic">
    <h4>Our Clinic</h4>
    <div class="clinic-cols">
      <div><b>Dee Why</b>71 Coral Parade, Suite 12<br>Dee Why, NSW 2099</div>
      <div><b>Leichhardt</b>Level 1<br>40 Ferris Lane 2040<br>Tel: 02 9000 4417</div>
      <div><b>Newcastle</b>9/5 Quarry St<br>Merewether, NSW 2291</div>
    </div>
  </div>
</footer>
<div class="legal">© Harbourline Institute of Cosmetic Surgery Dr Miles Ardent Cosmetic Surgery Sydney Australia 2016</div>

</body>
</html>
```